energy rating company

Web Design graphics and layout only

To create two pages for the website. First the home page and the second is the design for the job board for our clients use after login. I have attached files that explain in detail what the pages should have and the purpose/desires of each object. Please read these thoroughly.

The webpages need to be clean, professional, easy on the eye, obvious in all its buttons and functions with a strong call to action on the home page and branding and clean, great and obvious looking buttons and very simple but dynamic as well. We wish to be seen as contemporary.

Business Concept

Our business concept is simple, to build a website whereby our clients will be able to upload jobs for energy raters to quote on and subsequent complete the work if their quote is selected. To link energy ratings that are required with energy raters via our website. Similarly to the varn website, jobs will be “advertised” on the job board and raters will select which jobs they wish to quote for.

I have attached a Word document explaining all the parts of the website and another word document showing what we are sort of after and a excel spreadsheet as well. Please read these in conjunction with this brief!
Updates

Dear All

I have submitted with my brief a word doc and excel spreadsheet of the two pages I want created.  However this is not the layout or design I want, I only put it together so that you will need to know what is required on each page.  Feel free to change and redesign it all.

Also the second page does not require the "process" logo or any other menu items except the first five being Home, How it works, About Us, testimonials and Contact us as per the home page.

We also are looking for something very professional and very clean.  It should be very easy to see exactly what you are looking for.

I will also extend the deadline for new designers!!  I am excited to see your talents!!

Thanks

I have increase budget and posted a note saying feel free to change all the details layout etc on my brief just include everything!!! 

Wanting a professional corporate look...

Want a professional corporate look

We have changed our minds and you we no longer require the process to be on the home page.

Thanks

Target Market(s)

Target Market

Home Inspection Companies
Pest Inspection Companies
Residential home buyers/sellers
Real Estate companies

Industry/Entity Type

It Company

Number of Pages Required

1 page

Requirements
Must have
• Colours and Styles

• The website should be mainly white as I believe it is seen as clean and simple with colour from the logos, but can be swayed if it projects the image we are after.

• It should be obvious and process orientated and I do believe symbols, pictures, etc should replace words where possible.

```html
<!DOCTYPE html>
<html lang="en">
<head>
<meta charset="utf-8">
<title>voltrate australia – Energy Rating Quotes</title>
<link rel="stylesheet" href="https://fonts.googleapis.com/css2?family=Arimo:wght@400;700&family=Barlow+Semi+Condensed:wght@500&family=Open+Sans:wght@300;400;600&display=swap">
<style>
  :root {
    --ink: #111;
    --bar-dark: #1f2328;
    --page-bg: #f5f6f6;
    --nav-top: #f4f4f4;
    --nav-bottom: #d9d9d9;
    --nav-text: #4a4a4a;
    --teal: #0b7a5f;
    --lime: #a9c718;
    --sun: #f6c500;
    --welcome: #4fb27a;
    --brand: #2f9342;
    --accent: #e3701c;
    --search-btn: #f07a1d;
    --testimonial: #c6dc1f;
    --link: #2a2a2a;
    --quote-green: #2f9a3f;
    --rule: #9a9a9a;
  }
  * { box-sizing: border-box; margin: 0; padding: 0; }
  html, body { width: 1021px; height: 1200px; overflow: hidden; }
  body {
    background: var(--page-bg);
    font-family: "Arimo", Arial, sans-serif;
    color: var(--ink);
    position: relative;
  }

  /* top utility bar */
  .utility-bar { position: absolute; left: 0; top: 0; width: 1021px; height: 32px; background: var(--bar-dark); }
  .search-field { position: absolute; left: 738px; top: 10px; width: 156px; height: 15px; background: #fff; border: 1px solid #bbb; }
  .search-button {
    position: absolute; left: 900px; top: 10px; width: 54px; height: 15px;
    background: var(--search-btn); color: #fff; font: 700 8px "Arimo", sans-serif;
    letter-spacing: .5px; text-align: center; line-height: 15px;
  }

  /* main navigation */
  .main-nav {
    position: absolute; left: 0; top: 32px; width: 1021px; height: 41px;
    background: linear-gradient(var(--nav-top), var(--nav-bottom));
    border-bottom: 1px solid #c4c4c4;
  }
  .nav-list { position: absolute; left: 59px; top: 0; display: flex; height: 41px; list-style: none; }
  .nav-item {
    display: flex; align-items: center; justify-content: center; gap: 16px;
    height: 41px; border-right: 1px solid #c8c8c8;
    font: 500 20px "Barlow Semi Condensed", sans-serif; color: var(--nav-text);
    letter-spacing: -.2px;
  }
  .nav-item svg { width: 19px; height: 19px; }

  /* hero */
  .hero { position: absolute; left: 0; top: 74px; width: 1021px; height: 293px; background: #f7f8f8; }
  .hero-photo {
    position: absolute; left: 520px; top: 26px; width: 440px; height: 267px;
    background: linear-gradient(90deg, #f2f2f2 0%, #d9d4cf 30%, #3a3a3f 70%, #22252a 100%);
  }
  .brand { position: absolute; left: 84px; top: 150px; display: flex; align-items: center; gap: 12px; z-index: 1; }
  .brand-dot { width: 26px; height: 26px; border-radius: 50%; background: var(--accent); flex: none; }
  .brand-name { font: 600 36px "Open Sans", sans-serif; color: var(--brand); letter-spacing: -1px; white-space: nowrap; }

  /* service panels */
  .services { position: absolute; left: 59px; top: 367px; display: flex; }
  .service-card { position: relative; width: 301px; height: 214px; color: #fff; }
  .service-card.quote { background: var(--teal); }
  .service-card.raters { background: var(--lime); }
  .service-card.jobs { background: var(--sun); }
  .service-title { position: absolute; left: 18px; top: 17px; font: 300 35px "Open Sans", sans-serif; letter-spacing: -.5px; white-space: nowrap; }
  .service-text { position: absolute; left: 20px; top: 81px; width: 165px; font-size: 12px; line-height: 18px; }
  .service-art { position: absolute; left: 192px; top: 70px; width: 98px; height: 72px; border-radius: 6px; }
  .quote .service-art { background: linear-gradient(135deg, #f2f2f2, #c92a2a); }
  .raters .service-art { background: linear-gradient(135deg, #eef6d8, #9aa3ad); }
  .jobs .service-art { background: linear-gradient(135deg, #fff7d9, #4a9fd8); }
  .read-more {
    position: absolute; left: 95px; top: 162px; width: 116px; height: 34px;
    background: linear-gradient(#fafafa, #d4d4d4); border: 1px solid #b9b9b9; border-radius: 3px;
    display: flex; align-items: center; justify-content: center; gap: 8px;
    font: 700 12px "Arimo", sans-serif; color: #333;
  }
  .read-more svg { width: 20px; height: 20px; }

  /* welcome copy */
  .welcome { position: absolute; left: 61px; top: 598px; width: 650px; font-size: 12.5px; line-height: 18.7px; }
  .welcome h1 { font: 400 34px "Open Sans", sans-serif; color: var(--welcome); letter-spacing: -.6px; margin-bottom: 8px; line-height: 40px; }
  .benefits { list-style: none; margin: 10px 0 24px; }
  .benefits li { display: flex; align-items: center; gap: 5px; height: 24px; }
  .benefits li::before { content: ""; width: 12px; height: 12px; border-radius: 50%; background: var(--accent); flex: none; }

  /* sidebar */
  .sidebar-divider { position: absolute; left: 717px; top: 611px; width: 1px; height: 229px; background: var(--rule); }
  .login { position: absolute; left: 736px; top: 613px; width: 228px; }
  .login h2 { font: 400 23px "Open Sans", sans-serif; color: #2b2b2b; margin: 0 0 11px 5px; letter-spacing: .3px; }
  .field-label { display: block; font-size: 11px; margin-bottom: 2px; }
  .field-input { width: 227px; height: 17px; border: 1px solid #8a8a8a; border-radius: 2px; margin-bottom: 22px; background: #fff; }
  .login-button {
    position: absolute; left: 173px; top: 138px; width: 54px; height: 32px;
    background: linear-gradient(#fafafa, #d6d6d6); border: 1px solid #a8a8a8; border-radius: 3px;
    font: 400 12px "Arimo", sans-serif; text-align: center; line-height: 30px; color: #333;
  }
  .account-links { position: absolute; left: 0; top: 178px; font-size: 11px; line-height: 23px; }
  .account-links a { display: block; color: var(--link); text-decoration: underline; }
  .sidebar-rule { position: absolute; left: 727px; top: 846px; width: 241px; height: 1px; background: var(--rule); }

  .testimonial-badge { position: absolute; left: 732px; top: 859px; width: 241px; height: 80px; }
  .testimonial-badge span {
    position: absolute; left: 22px; top: 17px; font: 700 22px "Arimo", sans-serif; color: #fff; letter-spacing: -.3px;
  }
  .testimonial-text { position: absolute; left: 743px; top: 941px; width: 240px; font-size: 12.5px; line-height: 17.6px; }
  .testimonial-source { position: absolute; left: 743px; top: 1101px; width: 240px; font-size: 12.5px; line-height: 18px; color: var(--quote-green); }

  /* footer */
  .site-footer { position: absolute; left: 0; top: 1144px; width: 1021px; height: 32px; background: var(--bar-dark); color: #fff; font-size: 10.5px; }
  .footer-links { position: absolute; left: 61px; top: 9px; display: flex; list-style: none; }
  .footer-links li + li::before { content: "|"; margin: 0 8px; }
  .legal-links { position: absolute; right: 35px; top: 10px; display: flex; font-size: 9px; list-style: none; }
  .legal-links li + li::before { content: "|"; margin: 0 10px 0 14px; }
</style>
</head>
<body>
  <div class="utility-bar">
    <div class="search-field"></div>
    <div class="search-button">SEARCH</div>
  </div>

  <nav class="main-nav">
    <ul class="nav-list">
      <li class="nav-item" style="width:128px">HOME <svg viewBox="0 0 20 20"><circle cx="10" cy="10" r="9" fill="#b5b5b5"/><path d="M8 6l5 4-5 4z" fill="#eee"/></svg></li>
      <li class="nav-item" style="width:191px">HOW IT WORKS <svg viewBox="0 0 20 20"><circle cx="10" cy="10" r="9" fill="#b5b5b5"/><path d="M8 6l5 4-5 4z" fill="#eee"/></svg></li>
      <li class="nav-item" style="width:185px">ABOUT US <svg viewBox="0 0 20 20"><circle cx="10" cy="10" r="9" fill="#b5b5b5"/><path d="M8 6l5 4-5 4z" fill="#eee"/></svg></li>
      <li class="nav-item" style="width:189px">TESTIMONIALS <svg viewBox="0 0 20 20"><circle cx="10" cy="10" r="9" fill="#b5b5b5"/><path d="M8 6l5 4-5 4z" fill="#eee"/></svg></li>
      <li class="nav-item" style="width:188px">CONTACT US <svg viewBox="0 0 20 20"><circle cx="10" cy="10" r="9" fill="#b5b5b5"/><path d="M8 6l5 4-5 4z" fill="#eee"/></svg></li>
    </ul>
  </nav>

  <header class="hero">
    <div class="hero-photo" role="img" aria-label="Photo of a smiling businessman in a dark suit pointing towards the company name"></div>
    <div class="brand"><span class="brand-dot"></span><span class="brand-name">voltrate australia</span></div>
  </header>

  <section class="services">
    <article class="service-card quote">
      <h2 class="service-title">Get a quote</h2>
      <p class="service-text">Xerostie dit lor inim dip euguer sustrud tet dolore velis aliquam aliqui bla feu</p>
      <div class="service-art" role="img" aria-label="Illustration of a red computer mouse with a pointing hand cursor"></div>
      <a class="read-more">READ MORE <svg viewBox="0 0 20 20"><circle cx="10" cy="10" r="9" fill="#8c8c8c"/><path d="M8 6l5 4-5 4z" fill="#eee"/></svg></a>
    </article>
    <article class="service-card raters">
      <h2 class="service-title">Energy Raters</h2>
      <p class="service-text">Xerostie dit lor inim dip euguer sustrud tet dolore velis aliquam aliqui bla feu</p>
      <div class="service-art" role="img" aria-label="Illustration of an open book with a green seedling growing from it"></div>
      <a class="read-more">READ MORE <svg viewBox="0 0 20 20"><circle cx="10" cy="10" r="9" fill="#8c8c8c"/><path d="M8 6l5 4-5 4z" fill="#eee"/></svg></a>
    </article>
    <article class="service-card jobs">
      <h2 class="service-title">Active Job Board</h2>
      <p class="service-text">Xerostie dit lor inim dip euguer sustrud tet dolore velis aliquam aliqui bla</p>
      <div class="service-art" role="img" aria-label="Illustration of a rising bar chart on a clipboard"></div>
      <a class="read-more">READ MORE <svg viewBox="0 0 20 20"><circle cx="10" cy="10" r="9" fill="#8c8c8c"/><path d="M8 6l5 4-5 4z" fill="#eee"/></svg></a>
    </article>
  </section>

  <main class="welcome">
    <h1>Welcome</h1>
    <p>voltrate australia is Australia's leading professional energy rating consultancy firm specializing in large scaled residential and commercial energy rating logistics.<br>
    We have professional and accredited energy raters in all States and Territories ready and waiting to provide quotes for and perform &nbsp;your energy rating jobs!<br>
    It's Free, Fast and Easy to use and you get the best price and turnaround time that suits you!!<br>
    Register with us, upload your job and specifications, and sit back and watch as energy raters provide quotes for your work!</p>
    <ul class="benefits">
      <li>Get the best priced quotes for your energy ratings</li>
      <li>Save time by listing a job to get many quotes</li>
      <li>Monitor your jobs and quotes on your own job board</li>
      <li>Be notified via email of all new quotes as they come in</li>
      <li>Be able to specify your desired turnaround times</li>
      <li>Accessible anytime and anywhere</li>
      <li>Choose a deadline for energy raters to supply quotes</li>
      <li>Have access to many qualified energy raters in your state all quoting for your work</li>
      <li>Be able to track your jobs and pay online</li>
      <li>Provide feedback on energy raters</li>
    </ul>
    <p>Its totally free to be registered with us and there is no obligations or hidden catches! &nbsp;So if you wish to utilise the amazing opportunity register now! &nbsp;This new website will be going live on the (insert date) so be ready to save some money!</p>
  </main>

  <div class="sidebar-divider"></div>
  <aside class="login">
    <h2>USER LOGIN</h2>
    <label class="field-label">Username: *</label>
    <div class="field-input"></div>
    <label class="field-label">Password: *</label>
    <div class="field-input"></div>
    <div class="login-button">LOG IN</div>
    <div class="account-links">
      <a>Create new account</a>
      <a>Request new password</a>
    </div>
  </aside>
  <div class="sidebar-rule"></div>

  <div class="testimonial-badge">
    <svg width="241" height="80" viewBox="0 0 241 80">
      <path d="M8 0h225a8 8 0 0 1 8 8v48a8 8 0 0 1-8 8H34l-12 14V64H8a8 8 0 0 1-8-8V8a8 8 0 0 1 8-8z" fill="var(--testimonial)"/>
      <path d="M8 0h225a8 8 0 0 1 8 8v18H0V8a8 8 0 0 1 8-8z" fill="#d8e84a"/>
    </svg>
    <span>TESTIMONIALS</span>
  </div>
  <p class="testimonial-text">Xerostie dit lor inim dip euguer sustrud tet dolore velis aliquam aliqui bla feu feu faccum ip elis augiam erostrud tat Xerostie dit lor inim dip euguer sustrud tet dolore velis aliquam aliqui bla feu feu faccum ip elis augiam erostrud tat Xerostie dit lor inim dip euguer sustrud tet dolore velis</p>
  <p class="testimonial-source">aliquam aliqui bla feu feu faccum ip elis augiam erostrud tat</p>

  <footer class="site-footer">
    <ul class="footer-links">
      <li>home</li><li>about us</li><li>services</li><li>products</li><li>solutions</li><li>contacts</li>
    </ul>
    <ul class="legal-links"><li>Privacy policy</li><li>Site map</li></ul>
  </footer>
</body>
</html>
```